Bed & Breakfast Wordpress Theme - Design Only

We are looking for a Wordpress theme for an award winning UK Bed & Breakfast (Guesthouse) www.fernbrookinn.co.uk
You will see that the current site is basic and dated, we need a new site that showcases the very high standard of rooms on offer and is geared towards both mobile and desktop browsing.
We would like the colours that have been used in the rooms and building (as seen on the current website) to feature in the design.
We particularly like the look of this accommodation provider website: http://www.marlowdenbarns.co.uk
Selected website images can be downloaded here, feel free to use more from the existing website too:
https://www.filevaultly.com/s/qz81mv4rt7kw0pn/website%20images.zip
Target Market(s)
The accommodation is upmarket and the design needs to subtly communicate this.
The accommodation attracts a varied mix of ages so needs to be up scale without being overly modern.
Industry/Entity Type
Accommodation
Requirements
Must have
- As the accommodation does not have a logo we need a basic typographic logo incorporated into the design.
Colours of the building and rooms must be integrated into the design in some way.
A bold homepage that allows images of the rooms on offer and key information to be visibale above the fold. The goal of the homepage is for someone to then click Rooms or Prices so calls to action may help here.
Separate designs for a sidebar and full width version of sub pages.
An area that shows off the awards won by the company on all pages and space for testimonials.
The site must enable an easy transition from - homepage - to rooms - to prices with possible call to action buttons in the top right corner on these pages
The site needs to have a Homepage layout, a general sub page layout, and a 'Rooms' page layout which will showcase all rooms available possibly in a grid layout.
Nice to have
- Please use some of the images available currently on the website in your mockup, particularly of the building and rooms.
Should not have
- No need for any type of booking fields or engine as the booking system will be embedded on a full width page.

```html
<!DOCTYPE html>
<html lang="en">
<head>
<meta charset="utf-8">
<title>FernbrookInn – Rooms</title>
<link href="https://fonts.googleapis.com/css2?family=Noto+Serif:wght@400&family=Open+Sans:wght@400;600&display=swap" rel="stylesheet">
<style>
:root{
  --brown:#7b6c60;
  --dark:#4e4038;
  --text:#555;
  --line:#e2e2e2;
  --footer:#ececec;
  --white:#fff;
}
*{margin:0;padding:0;box-sizing:border-box}
html,body{width:917px;height:1200px;overflow:hidden;background:var(--white);font-family:"Open Sans",sans-serif;color:var(--text)}
.page{position:relative;width:917px;height:1200px}
.topbar{height:29px;background:var(--brown);color:#e3dbd4;font-size:8px;display:flex;align-items:center;padding:0 139px 0 153px}
.topbar .addr{flex:1}
.topbar b{font-weight:400;color:#fff}
.topbar .mail{margin-right:24px}
.header{height:57px;display:flex;align-items:center;padding:0 139px 0 152px;border-bottom:1px solid var(--line)}
.logo{font-family:"Noto Serif",serif;font-size:19px;color:var(--dark);flex:1}
.nav{display:flex;gap:27px;font-family:"Noto Serif",serif;font-size:9.5px;color:#666}
.titleband{height:58px;background:linear-gradient(180deg,#ececec,#f7f7f7 40%,#f1f1f1);display:flex;align-items:center;padding:0 148px 0 154px;border-bottom:1px solid var(--line)}
.titleband h1{flex:1;font-family:"Noto Serif",serif;font-weight:400;font-size:12.5px;color:#444}
.crumbs{font-size:7.5px;color:#666}
.tabs{position:absolute;top:174px;left:154px;width:616px;height:24px;border-top:1px solid var(--line);border-bottom:1px solid var(--line);display:flex;gap:29px;font-size:8.8px;color:#444;align-items:center}
.tabs span.active{font-weight:600;position:relative}
.tabs span.active::before{content:"";position:absolute;left:0;top:-8px;width:34px;height:2px;background:var(--brown)}
.grid{position:absolute;top:237px;left:154px;display:grid;grid-template-columns:repeat(4,144px);grid-template-rows:repeat(5,105px);column-gap:13px;row-gap:12px}
.tile{position:relative;overflow:hidden}
.exterior{background:linear-gradient(180deg,#8db3d9 0%,#c5d5e0 28%,#ebebe8 42%,#dedbd4 68%,#cdbb9c 100%)}
.staircase{background:radial-gradient(ellipse 30% 70% at 50% 45%,#e4e3d0 0%,#d9d6bf 55%,#8b5e3a 100%)}
.canopy-room{background:linear-gradient(165deg,#f1e9df 0%,#e6d9c7 55%,#b59985 82%,#d5c2a8 100%)}
.breakfast{background:linear-gradient(135deg,#c7857c 0%,#dcd2c7 40%,#a4a89a 70%,#a88d74 100%)}
.patio-room{background:linear-gradient(180deg,#8d7358 0%,#d2c6b2 35%,#e5e4dc 60%,#b6a38a 100%)}
.log-bed{background:linear-gradient(180deg,#d4c2a6 0%,#ecebe5 55%,#cdb597 100%)}
.garden-room{background:linear-gradient(180deg,#9a7d60 0%,#dde4d2 40%,#8fb06e 72%,#6f6a60 100%)}
.stove{background:linear-gradient(90deg,#3b3e4a 0%,#4b4e5b 38%,#e2dbd1 58%,#9a7e95 82%,#a4876a 100%)}
.overlay{position:absolute;inset:0;background:rgba(40,36,34,.62);display:flex;flex-direction:column;align-items:center;justify-content:center;color:#fff;text-align:center}
.overlay .zoom{width:22px;height:22px;border-radius:50%;background:#2e2a28;display:flex;align-items:center;justify-content:center;margin-bottom:6px}
.overlay h3{font-family:"Noto Serif",serif;font-weight:400;font-size:11px}
.overlay p{font-size:7px;line-height:10px;width:84px;margin-top:2px}
.pager{position:absolute;top:880px;right:147px;display:flex;align-items:center;gap:4px;font-size:7.5px;color:#555}
.pager .num{width:10px;height:10px;border:1px solid #aaa;font-size:6px;display:flex;align-items:center;justify-content:center}
.pager .num.cur{background:var(--brown);border-color:var(--brown);color:#fff}
.pager .prev{margin-right:8px}.pager .next{margin-left:8px}
.footer{position:absolute;top:966px;left:0;width:917px;height:195px;background:var(--footer)}
.fcol{position:absolute;top:33px;font-size:8.5px;color:#666}
.fcol h4{font-weight:400;font-size:8.8px;color:#333;margin-bottom:14px}
.flogo{font-family:"Noto Serif",serif;font-size:18px;color:var(--dark);margin-top:-10px;margin-bottom:5px}
.about{font-size:6.8px;line-height:13px;width:152px}
.social{display:flex;gap:12px;margin-top:4px}
.social span{width:10px;height:10px;border-radius:50%;background:#777}
.post{width:130px;border-bottom:1px solid #ccc;padding-bottom:6px;margin-bottom:14px}
.post small{font-size:5.5px;color:#777;display:block;margin-bottom:3px}
.post p{font-size:8.5px;line-height:13px;color:#777;width:128px}
.contacts p{line-height:13px;font-size:8.5px}
.bottombar{position:absolute;top:1161px;left:0;width:917px;height:39px;background:var(--dark);color:#d7ccc3;font-size:7.5px;display:flex;align-items:center;padding:0 147px 0 153px}
.bottombar .copy{flex:1}
</style>
</head>
<body>
<div class="page">
  <div class="topbar">
    <span class="addr">ADDRESS: <b>Fernbrook Inn, Mill Lane, Ashcombe, Hampshire SO41 2QD</b></span>
    <span class="mail">EMAIL: <b>enquiries@fernbrookinn.co.uk</b></span>
    <span>CALL US: <b>1-500-555-0142</b></span>
  </div>
  <header class="header">
    <div class="logo">FernbrookInn</div>
    <nav class="nav"><span>Home</span><span>Rooms</span><span>Prices</span><span>Picture Gallery</span><span>Information</span><span>Contact</span></nav>
  </header>
  <div class="titleband"><h1>Rooms</h1><span class="crumbs">Home &nbsp;/&nbsp; Rooms</span></div>

  <div class="tabs">
    <span class="active">All Rooms</span><span>Small Doubles/Singles</span><span>Doubles</span><span>Twin</span><span>Four Poster</span><span>Triples</span><span>Dog Friendly</span>
  </div>

  <div class="grid">
    <div class="tile exterior" role="img" aria-label="Photo: white-painted lodge exterior with yellow front door under blue sky"></div>
    <div class="tile staircase" role="img" aria-label="Photo: wooden staircase leading up to a cream cottage door"></div>
    <div class="tile canopy-room" role="img" aria-label="Photo: bright attic bedroom with white four-poster bed"></div>
    <div class="tile breakfast" role="img" aria-label="Photo: breakfast table set with sage-green teapot"></div>

    <div class="tile patio-room" role="img" aria-label="Photo: bedroom with carved bed post and open patio doors"></div>
    <div class="tile log-bed" role="img" aria-label="Photo: rustic driftwood four-poster bed with white linen"></div>
    <div class="tile garden-room" role="img" aria-label="Photo: room with open doors onto a green garden view">
      <div class="overlay">
        <div class="zoom"><svg width="10" height="10" viewBox="0 0 10 10"><circle cx="4" cy="4" r="3" fill="none" stroke="#fff" stroke-width="1.4"/><line x1="6.2" y1="6.2" x2="9" y2="9" stroke="#fff" stroke-width="1.6"/></svg></div>
        <h3>Room Name</h3>
        <p>Short description about the room</p>
      </div>
    </div>
    <div class="tile stove" role="img" aria-label="Photo: cast-iron wood stove beside a purple-cushioned wicker chair"></div>

    <div class="tile exterior" role="img" aria-label="Photo: white-painted lodge exterior with yellow front door under blue sky"></div>
    <div class="tile staircase" role="img" aria-label="Photo: wooden staircase leading up to a cream cottage door"></div>
    <div class="tile canopy-room" role="img" aria-label="Photo: bright attic bedroom with white four-poster bed"></div>
    <div class="tile breakfast" role="img" aria-label="Photo: breakfast table set with sage-green teapot"></div>

    <div class="tile patio-room" role="img" aria-label="Photo: bedroom with carved bed post and open patio doors"></div>
    <div class="tile log-bed" role="img" aria-label="Photo: rustic driftwood four-poster bed with white linen"></div>
    <div class="tile garden-room" role="img" aria-label="Photo: room with open doors onto a green garden view"></div>
    <div class="tile stove" role="img" aria-label="Photo: cast-iron wood stove beside a purple-cushioned wicker chair"></div>

    <div class="tile exterior" role="img" aria-label="Photo: white-painted lodge exterior with yellow front door under blue sky"></div>
    <div class="tile staircase" role="img" aria-label="Photo: wooden staircase leading up to a cream cottage door"></div>
    <div class="tile canopy-room" role="img" aria-label="Photo: bright attic bedroom with white four-poster bed"></div>
    <div class="tile breakfast" role="img" aria-label="Photo: breakfast table set with sage-green teapot"></div>
  </div>

  <div class="pager">
    <span class="prev">‹ Previous</span>
    <span class="num cur">1</span><span class="num">2</span><span class="num">3</span><span class="num">4</span><span class="num">5</span><span class="num">6</span>
    <span class="next">Next ›</span>
  </div>

  <footer class="footer">
    <div class="fcol" style="left:152px">
      <div class="flogo">FernbrookInn</div>
      <p class="about">Award-Winning, Eco Chic,<br>Environmentally-Responsible, New Forest<br>Accommodation offering 24 hour front<br>desk, daily housekeeping, private</p>
      <h4 style="margin-top:34px;margin-bottom:8px">GET SOCIAL</h4>
      <div class="social"><span></span><span></span><span></span><span></span><span></span></div>
    </div>
    <div class="fcol" style="left:310px">
      <h4>RECENT POSTS</h4>
      <div class="post"><small>DEC 15, 2012 &nbsp;|&nbsp; BY ADMIN</small><p>Morbi a libero eget erat auctor<br>Sus vitae id tortor suspendisse.<br>Vestibulum eu ligula lorem ...</p></div>
      <div class="post"><small>DEC 15, 2012 &nbsp;|&nbsp; BY ADMIN</small><p>Morbi a libero eget erat auctor<br>Sus vitae id tortor suspendisse.<br>Vestibulum eu ligula lorem ...</p></div>
    </div>
    <div class="fcol contacts" style="left:468px">
      <h4>CONTACTS</h4>
      <p>Harlow &amp; Reed Ltd.<br>PO Box 40312<br>Carrow Lane, Bristol<br>Avon BS1 4QT England</p>
      <p style="margin-top:13px">Phone: (415) 555-0187<br>Fax: (415) 555-0188</p>
      <p style="margin-top:13px">support@fernbrookinn.co.uk</p>
    </div>
    <div class="fcol" style="left:625px">
      <h4>AWARDS</h4>
      <svg width="140" height="130" viewBox="0 0 140 130">
        <rect x="0" y="0" width="40" height="62" rx="3" fill="#d9c9ae"/>
        <circle cx="80" cy="28" r="24" fill="#2f3a6b"/>
        <rect x="0" y="78" width="130" height="46" rx="3" fill="#d8d2c7"/>
      </svg>
    </div>
  </footer>

  <div class="bottombar">
    <span class="copy">© 2014 FernbrookInn. All Rights Reserved</span>
    <span>Home | Rooms | Tariffs | Activities | Eating &amp; Drinking | Travel | Links | Sitemap</span>
  </div>
</div>
</body>
</html>
```